Up to the Challenge? Canadian based consulting company needs a two sided business card design

A Canadian based security risk management consulting company needs a two-sided business card design. What we do is provide advice and guidance related to emergency, security and business continuity management for small, medium and large companies to help ensure the protection of their people, assets, information, services, operations and reputation.

The final design should be simple, only one or two colours, eye catching, professional and one that makes people look at three or more times just because it looks so darn good.

I have include examples of business cards I like.

Target Market(s)

Small, medium and large companies.

Industry/Entity Type

Security

Contact Information for Business Card

Business Card Size: Standard size of 3.5" (89mm) x 2.0" (51mm) - (see full specifications and guides on PRINTA's website if required)
Card Stock: Looking to use PRINTA's Velda 32pt stock textured paper - seam colour either chili red or black
Business Name: The Harrowfield Group
Website: www.theharrowfieldgroup.example
Telephone: (555)214-0397
Name: Dana Forsythe
Position: Principle
e-mail: Dana.Forsythe@theharrowfieldgroup.example

Font styles to use
Serif

Colors
ec1f27
000000
9d9d9d
aaaaaa
606060

Requirements
Must have
• - "The Harrowfield Group" logo (see uploaded files). I have included grey scale and colour versions.
• - Business card details (as above)
Nice to have
• - One side black or grey scale.
• - Other side would likely be white.
• - Everyone likes the silver logo on the black background.
• - Small element of colour i.e. red but I'm leaning more to greyscale.
Should not have
• - A lot of colour. Keep it simple.

```html
<!DOCTYPE html>
<html lang="en">
<head>
<meta charset="utf-8">
<title>The Harrowfield Group – Business Card</title>
<link rel="stylesheet" href="https://fonts.googleapis.com/css2?family=Libre+Baskerville:wght@400;700&family=Montserrat:wght@400;500&display=swap">
<style>
  :root {
    --backdrop: #2a2a2a;
    --card: #ffffff;
    --ink: #000000;
    --grey-dark: #606060;
    --grey-mid: #9d9d9d;
    --grey-light: #aaaaaa;
    --mark: #8a8a8a;
  }
  * { box-sizing: border-box; margin: 0; padding: 0; }
  html, body {
    width: 1200px; height: 1000px; overflow: hidden;
    background: var(--backdrop);
  }
  .stage {
    position: relative; width: 1200px; height: 1000px;
  }
  .card {
    position: absolute; left: 250px; width: 700px; height: 400px;
    background: var(--card); border-radius: 22px; overflow: hidden;
  }
  .card--front { top: 70px; }
  .card--back { top: 530px; }

  /* Front */
  .front-brand {
    position: absolute; left: 0; right: 0; top: 150px;
    display: flex; align-items: center; justify-content: center; gap: 18px;
  }
  .brand-square {
    width: 44px; height: 44px; background: var(--mark);
  }
  .brand-name {
    font-family: "Libre Baskerville", serif; font-weight: 400;
    font-size: 30px; letter-spacing: 2px; color: var(--mark);
    text-transform: uppercase; line-height: 1;
  }
  .front-profile {
    position: absolute; left: 40px; bottom: 34px;
    font-family: "Montserrat", sans-serif; font-size: 15px;
    color: var(--ink); letter-spacing: 0.3px;
  }

  /* Back */
  .back-brand {
    position: absolute; left: 48px; top: 48px;
    font-family: "Libre Baskerville", serif; font-weight: 400;
    font-size: 19px; letter-spacing: 1.5px; color: var(--grey-mid);
    text-transform: uppercase;
  }
  .back-rule {
    position: absolute; left: 48px; top: 84px; width: 240px; height: 1px;
    background: var(--grey-mid);
  }
  .person-name {
    position: absolute; left: 78px; top: 102px;
    font-family: "Libre Baskerville", serif; font-weight: 700;
    font-size: 25px; color: var(--grey-dark);
  }
  .person-role {
    position: absolute; left: 78px; top: 140px;
    font-family: "Montserrat", sans-serif; font-weight: 500;
    font-size: 14px; color: var(--ink);
  }
  .accent-bar {
    position: absolute; left: 0; top: 118px; width: 36px; height: 46px;
    background: var(--ink);
  }
  .contact-list {
    position: absolute; left: 78px; top: 176px; list-style: none;
    font-family: "Montserrat", sans-serif; font-size: 14px;
    color: var(--grey-dark);
  }
  .contact-list li {
    display: flex; align-items: center; gap: 10px; height: 24px;
  }
  .contact-list svg { width: 12px; height: 12px; fill: var(--grey-dark); flex: none; }
  .back-mark {
    position: absolute; right: 58px; top: 76px;
    width: 96px; height: 96px; background: var(--mark);
  }
</style>
</head>
<body>
<main class="stage">

  <section class="card card--front" aria-label="Business card front">
    <div class="front-brand">
      <span class="brand-square" aria-hidden="true"></span>
      <span class="brand-name">The Harrowfield Group</span>
    </div>
    <p class="front-profile">profile: https://ca.profiles.example/in/danaforsythe</p>
  </section>

  <section class="card card--back" aria-label="Business card back">
    <p class="back-brand">The Harrowfield Group</p>
    <span class="back-rule" aria-hidden="true"></span>
    <span class="accent-bar" aria-hidden="true"></span>
    <h1 class="person-name">Dana Forsythe</h1>
    <p class="person-role">Principle</p>
    <ul class="contact-list">
      <li>
        <svg viewBox="0 0 12 12" aria-hidden="true"><path d="M2.4 0.6l2 2-1 1.3c.7 1.5 1.9 2.7 3.4 3.4l1.3-1 2 2-1.4 1.8C4.9 9.8 2.2 7.1 0.6 2.2z"/></svg>
        (555)214-0397
      </li>
      <li>
        <svg viewBox="0 0 12 12" aria-hidden="true"><path d="M0.5 2.5h11v7h-11z M1.3 3.2l4.7 3.4 4.7-3.4v-0.2H1.3z" fill-rule="evenodd"/></svg>
        Dana.Forsythe@theharrowfieldgroup.example
      </li>
      <li>
        <svg viewBox="0 0 12 12" aria-hidden="true"><circle cx="6" cy="6" r="5.2" fill="none" stroke="#606060" stroke-width="1.1"/><path d="M0.8 6h10.4M6 0.8c-2.6 3-2.6 7.4 0 10.4M6 0.8c2.6 3 2.6 7.4 0 10.4" fill="none" stroke="#606060" stroke-width="0.9"/></svg>
        www.theharrowfieldgroup.example
      </li>
    </ul>
    <span class="back-mark" aria-hidden="true"></span>
  </section>

</main>
</body>
</html>
```